Renewable energy website needs a wordpress website

We are a Renewable Energy company specialising in Energy Management, LED Lights and Solar PV Systems based in Kuala Lumpur.
We need wordpress website designed to match our company identity.
We would like to stick with similar shades of blue & green as our logo and to keep it fresh and creative at the same time.

It Company

```html
<!DOCTYPE html>
<html lang="en">
<head>
<meta charset="utf-8">
<title>Verdanta Power – Website Presentation</title>
<link rel="stylesheet" href="https://fonts.googleapis.com/css2?family=Open+Sans:wght@300;400;600;700&family=Roboto:wght@300&display=swap">
<style>
:root{
  --board-bg:#ffffff;
  --page-bg:#ffffff;
  --ink:#222222;
  --text:#5a5a5a;
  --muted:#8a8a8a;
  --cyan:#16d0ee;
  --green:#1f5a1e;
  --brand:#2aa6c9;
  --contact-bg:#efefef;
  --field:#ffffff;
  --footer-dark:#2c3a40;
  --dim-page:#6b6b6b;
  --dim-text:#3a3a3a;
  --dim-teal:#0c6b7b;
  --dim-green:#143814;
  --dim-photo:#4a5358;
  --arrow:#9fdff0;
  --note:#3a3a3a;
}
*{margin:0;padding:0;box-sizing:border-box}
html,body{width:1200px;height:1045px;overflow:hidden;background:var(--board-bg)}
body{font-family:"Open Sans",Arial,sans-serif;color:var(--text)}
.board{position:relative;width:1200px;height:1045px;overflow:hidden}

/* ---------- full page ---------- */
.site{position:absolute;left:53px;top:33px;width:463px;height:949px;background:var(--page-bg);box-shadow:0 6px 22px rgba(0,0,0,.45);overflow:hidden}
.site-header{position:absolute;left:0;top:0;width:100%;height:26px;background:#fff}
.brand{position:absolute;display:flex;align-items:center;gap:3px;font-weight:700;color:var(--brand);text-transform:uppercase;white-space:nowrap}
.brand-dot{border-radius:50%;background:var(--brand);flex:none}
.site-header .brand{left:86px;top:8px;font-size:5px;letter-spacing:.3px}
.site-header .brand-dot{width:9px;height:9px}
.main-nav{position:absolute;left:207px;top:11px;display:flex;gap:6px;font-size:4px;font-weight:700;color:#333;text-transform:uppercase;letter-spacing:.2px}
.nav-icon{position:absolute;left:363px;top:10px;width:8px;height:8px}

.hero{position:absolute;left:0;top:26px;width:100%;height:148px;background:linear-gradient(180deg,#55636f 0%,#76838c 45%,#6b7560 78%,#3e4a2c 100%);clip-path:polygon(0 0,100% 0,100% 93%,50% 100%,0 93%)}
.hero-shade{position:absolute;inset:0;background:rgba(0,0,0,.25)}
.hero .brand{left:50%;top:32px;transform:translateX(-50%);font-size:8px;color:#5cc7e6;letter-spacing:.5px}
.hero .brand-dot{width:18px;height:18px;background:#5cc7e6}
.hero-title{position:absolute;left:0;width:100%;top:82px;text-align:center;color:#fff;font-size:6px;font-weight:700;letter-spacing:.6px;line-height:8px}
.hero-title span{display:block;font-weight:300;letter-spacing:.8px}
.hero-sub{position:absolute;left:0;width:100%;top:124px;text-align:center;color:#d8dde0;font-size:3.6px}
.hero-arrow{position:absolute;top:59px;width:7px;height:12px}
.hero-arrow.left{left:93px}.hero-arrow.right{left:364px}
.dots{position:absolute;left:50%;transform:translateX(-50%);display:flex;gap:3px}
.dots i{display:block;width:2px;height:2px;border-radius:50%;background:rgba(255,255,255,.55)}
.dots i.on{background:#fff}
.hero .dots{top:141px}

.band{position:absolute;left:0;width:100%;background:var(--cyan)}
.band-led{top:355px;height:210px;clip-path:polygon(0 3%,100% 0,100% 96%,0 100%)}
.band-end{top:760px;height:40px;clip-path:polygon(0 20%,100% 0,100% 100%,0 100%)}

.btn{position:absolute;left:204px;width:53px;height:11px;background:var(--green);color:#fff;font-size:3.6px;font-weight:600;text-transform:uppercase;display:flex;align-items:center;justify-content:center;letter-spacing:.3px}

.feature{position:absolute;left:0;width:100%;height:165px}
.feature-title{position:absolute;left:0;top:0;width:100%;text-align:center;font-size:5.2px;font-weight:700;color:var(--ink);letter-spacing:.3px;text-transform:uppercase}
.feature-photo{position:absolute;top:16px;width:137px;height:136px}
.photo-wind{background:linear-gradient(180deg,#4d7fc7 0%,#7fa8dc 55%,#b5b08a 78%,#6b6a3c 100%)}
.photo-led{background:radial-gradient(circle at 40% 45%,#3aa3e0 0%,#2d7a3a 25%,#7a2a8a 45%,#101018 75%)}
.feature-text{position:absolute;top:18px}
.text-block{height:51px;text-align:center}
.text-block h4{font-size:6px;font-weight:300;color:#555;text-transform:uppercase;letter-spacing:.3px;line-height:8px}
.text-block p{font-size:3.4px;line-height:4.3px;color:#666;margin-top:3px;text-align:left}
.photo-right .feature-photo{left:239px}
.photo-right .feature-text{left:86px;width:137px}
.photo-left .feature-photo{left:86px}
.photo-left .feature-text{left:234px;width:141px}
.band-led .text-block h4,.on-cyan .text-block h4{color:#0a4f5c}
.on-cyan .text-block p{color:#0b4855}

.contact{position:absolute;left:0;top:799px;width:100%;height:94px;background:var(--contact-bg)}
.contact h3{position:absolute;left:86px;top:14px;font-size:5px;font-weight:700;color:var(--ink)}
.field{position:absolute;left:86px;width:83px;height:9px;background:var(--field);font-size:3.2px;color:#999;padding:2px 3px}
.field-message{left:182px;top:29px;width:104px;height:39px}
.send{position:absolute;left:241px;top:81px;width:44px;height:9px;background:var(--green);color:#fff;font-size:3.4px;font-weight:600;display:flex;align-items:center;justify-content:center;text-transform:uppercase}
.team-label{position:absolute;left:303px;top:15px;font-size:3.6px;color:#666;text-transform:uppercase}
.team-grid{position:absolute;left:303px;top:31px;display:grid;grid-template-columns:repeat(3,18px);gap:5px 8px}
.member{width:18px;height:18px;background:linear-gradient(180deg,#d9d9d9,#7d7d7d)}
.member.active{background:linear-gradient(180deg,#7fe6f6,#2fbfdb)}

.site-footer{position:absolute;left:0;top:893px;width:100%;height:35px;background:linear-gradient(180deg,#3a4a52,#27333a 60%,#3d4630);display:flex;align-items:center;justify-content:center;color:#fff;font-size:6px;font-weight:700;letter-spacing:.5px}
.site-footer span{color:#9aa4a8;font-weight:400;margin-left:2px}
.site-bottom{position:absolute;left:0;top:928px;width:100%;height:21px;background:#fff;font-size:3.6px;color:#777;text-transform:uppercase}
.site-bottom span{position:absolute;top:8px}

/* ---------- popup states ---------- */
.note{position:absolute;left:597px;width:536px;text-align:center;font-family:"Roboto",Arial,sans-serif;font-weight:300;font-size:20px;color:var(--note);text-decoration:underline;text-underline-offset:3px;line-height:24px}
.note-project{top:154px}.note-team{top:559px}

.shot{position:absolute;left:597px;width:536px;background:var(--dim-page);overflow:hidden;box-shadow:0 4px 14px rgba(0,0,0,.4)}
.shot-project{top:205px;height:322px}
.shot-team{top:608px;height:304px}
.shot .abs{position:absolute}
.shot-hero{left:0;top:0;width:100%;height:15px;background:#1c2a2c;clip-path:polygon(0 0,100% 0,100% 80%,50% 100%,0 80%)}
.shot-hero .dots{top:7px}
.shot-hero .dots i{background:#555}.shot-hero .dots i.on{background:#888}
.dim-title{width:100%;left:0;text-align:center;font-size:5.6px;font-weight:700;color:#262626;text-transform:uppercase;letter-spacing:.3px}
.dim-photo{background:linear-gradient(180deg,#2d4566,#44546a 55%,#555544 80%,#33331e)}
.dim-col .text-block h4{color:#333}
.dim-col .text-block p{color:#2f2f2f;font-size:3.8px;line-height:4.8px}
.dim-teal{background:var(--dim-teal)}
.dim-btn{background:var(--dim-green);color:#777;font-size:4px;font-weight:600;display:flex;align-items:center;justify-content:center;text-transform:uppercase}
.dim-heading{font-size:6px;font-weight:300;color:#2e2e2e;text-transform:uppercase}
.dim-black{background:#0b0b0b}
.dim-contact{background:#666}
.dim-field{background:#777;font-size:3.4px;color:#444;padding:2px 3px}
.dim-member{width:16px;height:16px;background:#5a5a5a}
.dim-member.active{background:#1d7f90}
.dim-footer{background:#1f272a;display:flex;align-items:flex-end;justify-content:center;padding-bottom:7px;color:#8c979b;font-size:7px;font-weight:700;letter-spacing:.5px}
.dim-footer span{color:#5d6a6f;font-weight:400;margin-left:2px}
.dim-bottom{background:#5e5e5e;font-size:4px;color:#333;text-transform:uppercase}
.dim-bottom span{position:absolute;top:9px}

.modal{position:absolute;left:157px;width:223px;background:#fff;box-shadow:0 2px 10px rgba(0,0,0,.35)}
.modal-media{position:absolute;left:50%;transform:translateX(-50%)}
.media-solar{top:7px;width:140px;height:97px;background:linear-gradient(160deg,#9ec8ee 0%,#c8dcef 30%,#2d3f66 45%,#1e2b4a 75%,#5b6a80 100%)}
.media-portrait{top:5px;width:97px;height:97px;background:linear-gradient(180deg,#e8e8e8,#9a9a9a 60%,#4a4a4a)}
.modal h5{position:absolute;left:0;width:100%;text-align:center;font-size:5.8px;font-weight:400;color:#444}
.modal p{position:absolute;left:22px;width:179px;font-size:3.5px;line-height:4.6px;color:#666;text-align:center}
.modal-link{position:absolute;right:10px;font-size:4.4px;color:#555;text-decoration:underline}
.modal-arrow{position:absolute;width:6px;height:14px}
</style>
</head>
<body>
<div class="board">

  <!-- Full page layout -->
  <div class="site">
    <header class="site-header">
      <div class="brand"><span class="brand-dot"></span>Verdanta Power</div>
      <nav class="main-nav"><span>Energy Management</span><span>LED Lights</span><span>Solar PV Systems</span><span>Contacts</span><span>Team</span></nav>
      <svg class="nav-icon" viewBox="0 0 8 8"><circle cx="4" cy="4" r="3" fill="none" stroke="#16d0ee" stroke-width=".8"/><line x1="1" y1="4" x2="7" y2="4" stroke="#16d0ee" stroke-width=".6"/></svg>
    </header>

    <section class="hero" role="img" aria-label="Wind turbines on a green field under a cloudy sky">
      <div class="hero-shade"></div>
      <div class="brand"><span class="brand-dot"></span>Verdanta Power</div>
      <h1 class="hero-title">Reneable Energy Systems<span>Because We Care</span></h1>
      <div class="hero-sub">Learn more about our work</div>
      <svg class="hero-arrow left" viewBox="0 0 7 12"><polyline points="6,1 1,6 6,11" fill="none" stroke="#fff" stroke-width=".8"/></svg>
      <svg class="hero-arrow right" viewBox="0 0 7 12"><polyline points="1,1 6,6 1,11" fill="none" stroke="#fff" stroke-width=".8"/></svg>
      <div class="dots"><i></i><i class="on"></i><i></i></div>
    </section>

    <section class="feature photo-left" style="top:200px">
      <h2 class="feature-title">Energy Management</h2>
      <div class="feature-photo photo-wind" role="img" aria-label="Wind turbine on a grassy hill under a blue sky"></div>
      <div class="feature-text">
        <div class="text-block"><h4>Team</h4><p>Our engineers audit every site, measure real consumption and design a plan that cuts waste without cutting comfort. We then stay on to track results month after month, tune each system as needs change and report savings in plain numbers that owners can check.</p></div>
        <div class="text-block"><h4>Clients</h4><p>We work with offices, factories, hotels and homes across the region, from single rooftops to full campus upgrades. Every client gets one contact person, a clear quote before any work begins and honest advice on which upgrade pays back first and which one can wait.</p></div>
        <div class="text-block"><h4>Work</h4><p>Each project starts with data and ends with lower bills, fewer emissions and a system our clients can run themselves. We handle permits, installation, testing and training, so the switch to clean energy is quick, tidy and easy to live with from day one.</p></div>
      </div>
    </section>

    <div class="band band-led"></div>
    <div class="btn" style="top:372px">Contact us</div>

    <section class="feature photo-right on-cyan" style="top:401px">
      <h2 class="feature-title">LED Lights</h2>
      <div class="feature-photo photo-led" role="img" aria-label="Tangle of glowing multicoloured LED string lights"></div>
      <div class="feature-text">
        <div class="text-block"><h4>Team</h4><p>Our engineers audit every site, measure real consumption and design a plan that cuts waste without cutting comfort. We then stay on to track results month after month, tune each system as needs change and report savings in plain numbers that owners can check.</p></div>
        <div class="text-block"><h4>Clients</h4><p>We work with offices, factories, hotels and homes across the region, from single rooftops to full campus upgrades. Every client gets one contact person, a clear quote before any work begins and honest advice on which upgrade pays back first and which one can wait.</p></div>
        <div class="text-block"><h4>Work</h4><p>Each project starts with data and ends with lower bills, fewer emissions and a system our clients can run themselves. We handle permits, installation, testing and training, so the switch to clean energy is quick, tidy and easy to live with from day one.</p></div>
      </div>
    </section>

    <div class="btn" style="top:575px">Contact us</div>

    <section class="feature photo-left" style="top:605px">
      <h2 class="feature-title">Energy Management</h2>
      <div class="feature-photo photo-wind" role="img" aria-label="Wind turbine on a grassy hill under a blue sky"></div>
      <div class="feature-text">
        <div class="text-block"><h4>Team</h4><p>Our engineers audit every site, measure real consumption and design a plan that cuts waste without cutting comfort. We then stay on to track results month after month, tune each system as needs change and report savings in plain numbers that owners can check.</p></div>
        <div class="text-block"><h4>Clients</h4><p>We work with offices, factories, hotels and homes across the region, from single rooftops to full campus upgrades. Every client gets one contact person, a clear quote before any work begins and honest advice on which upgrade pays back first and which one can wait.</p></div>
        <div class="text-block"><h4>Work</h4><p>Each project starts with data and ends with lower bills, fewer emissions and a system our clients can run themselves. We handle permits, installation, testing and training, so the switch to clean energy is quick, tidy and easy to live with from day one.</p></div>
      </div>
    </section>

    <div class="band band-end"></div>
    <div class="btn" style="top:777px">Contact us</div>

    <section class="contact">
      <h3>CONTACT US</h3>
      <div class="field" style="top:31px">Name</div>
      <div class="field" style="top:45px">Email</div>
      <div class="field" style="top:59px">Phone</div>
      <div class="field field-message">Comment</div>
      <div class="send">Send letter</div>
      <div class="team-label">Our team</div>
      <div class="team-grid">
        <div class="member" role="img" aria-label="Team member portrait"></div>
        <div class="member active" role="img" aria-label="Team member portrait, selected"></div>
        <div class="member" role="img" aria-label="Team member portrait"></div>
        <div class="member" role="img" aria-label="Team member portrait"></div>
        <div class="member" role="img" aria-label="Team member portrait"></div>
      </div>
    </section>

    <footer class="site-footer" role="img" aria-label="Dark landscape banner">USE RENEABLE ENERGY SYSTEMS,<span>HELP THE PLANET</span></footer>
    <div class="site-bottom">
      <span style="left:86px">Orchid Lane, KL</span>
      <span style="left:205px">info@verdantapower.com</span>
      <span style="left:303px">(0035) 200 14 55 90</span>
    </div>
  </div>

  <!-- Project popup state -->
  <p class="note note-project">This window appears when you click on a project picture</p>
  <div class="shot shot-project">
    <div class="abs shot-hero"><div class="dots"><i></i><i class="on"></i><i></i></div></div>
    <div class="abs dim-title" style="top:40px">Energy Management</div>
    <div class="abs dim-photo" style="left:101px;top:60px;width:76px;height:170px" role="img" aria-label="Wind turbine photo, dimmed"></div>
    <div class="abs dim-col" style="left:330px;top:60px;width:190px">
      <div class="text-block" style="height:60px"><h4>Team</h4><p>Our engineers audit every site, measure real consumption and design a plan that cuts waste without cutting comfort. We then stay on to track results month after month, tune each system as needs change and report savings in plain numbers that owners can check.</p></div>
      <div class="text-block" style="height:60px"><h4>Clients</h4><p>We work with offices, factories, hotels and homes across the region, from single rooftops to full campus upgrades. Every client gets one contact person, a clear quote before any work begins and honest advice on which upgrade pays back first and which one can wait.</p></div>
      <div class="text-block"><h4>Work</h4><p>Each project starts with data and ends with lower bills, fewer emissions and a system our clients can run themselves. We handle permits, installation, testing and training, so the switch to clean energy is quick, tidy and easy to live with from day one.</p></div>
    </div>
    <div class="abs dim-teal" style="left:0;top:234px;width:100%;height:90px;clip-path:polygon(0 6%,100% 0,100% 100%,0 100%)"></div>
    <div class="abs dim-btn" style="left:238px;top:251px;width:62px;height:11px">Contact us</div>
    <div class="abs dim-title" style="top:280px">LED Lights</div>
    <div class="abs dim-heading" style="left:172px;top:302px">Team</div>
    <div class="abs dim-black" style="left:278px;top:303px;width:157px;height:20px" role="img" aria-label="LED lights photo, dimmed"></div>

    <div class="modal" style="top:82px;height:166px">
      <div class="modal-media media-solar" role="img" aria-label="Rows of solar panels under a blue sky"></div>
      <svg class="modal-arrow" style="left:11px;top:47px" viewBox="0 0 6 14"><polyline points="5,1 1,7 5,13" fill="none" stroke="#9fdff0" stroke-width=".8"/></svg>
      <svg class="modal-arrow" style="right:11px;top:47px" viewBox="0 0 6 14"><polyline points="1,1 5,7 1,13" fill="none" stroke="#9fdff0" stroke-width=".8"/></svg>
      <h5 style="top:110px">Solar Batteries</h5>
      <p style="top:123px">Our solar panels charge quiet battery banks during the day, so the building keeps running on clean power long after sunset. Every system comes with live monitoring, a yearly service visit and a clear report that shows how much energy was stored, used and saved.</p>
      <span class="modal-link" style="top:155px">Learn more</span>
    </div>
  </div>

  <!-- Team popup state -->
  <p class="note note-team">This window appears when you click on one of team member’s photo</p>
  <div class="shot shot-team">
    <div class="abs dim-photo" style="left:101px;top:0;width:90px;height:93px" role="img" aria-label="Wind turbine photo, dimmed"></div>
    <div class="abs dim-col" style="left:276px;top:-4px;width:158px">
      <div class="text-block" style="height:55px"><p>We work with offices, factories, hotels and homes across the region, from single rooftops to full campus upgrades. Every client gets one contact person, a clear quote before any work begins and honest advice on which upgrade pays back first and which one can wait.</p></div>
      <div class="text-block"><h4>Work</h4><p>Each project starts with data and ends with lower bills, fewer emissions and a system our clients can run themselves. We handle permits, installation, testing and training, so the switch to clean energy is quick, tidy and easy to live with from day one.</p></div>
    </div>
    <div class="abs dim-teal" style="left:0;top:96px;width:100%;height:46px;clip-path:polygon(0 0,100% 12%,100% 100%,0 88%)"></div>
    <div class="abs dim-contact" style="left:0;top:138px;width:100%;height:113px"></div>
    <div class="abs" style="left:101px;top:157px;font-size:6px;font-weight:700;color:#2a2a2a">CONTACT US</div>
    <div class="abs dim-field" style="left:101px;top:176px;width:53px;height:9px">Name</div>
    <div class="abs dim-field" style="left:101px;top:193px;width:53px;height:9px">Email</div>
    <div class="abs dim-field" style="left:101px;top:210px;width:53px;height:9px">Phone</div>
    <div class="abs dim-member active" style="left:392px;top:175px" role="img" aria-label="Team member portrait, selected"></div>
    <div class="abs dim-member" style="left:416px;top:175px" role="img" aria-label="Team member portrait"></div>
    <div class="abs dim-member" style="left:392px;top:200px" role="img" aria-label="Team member portrait"></div>
    <div class="abs dim-footer" style="left:0;top:251px;width:100%;height:32px">USE RENEABLE ENERGY SYSTEMS,<span>HELP THE PLANET</span></div>
    <div class="abs dim-bottom" style="left:0;top:283px;width:100%;height:21px">
      <span style="left:101px">Orchid Lane, KL</span>
      <span style="left:238px">info@verdantapower.com</span>
      <span style="left:400px">(0035) 200 14 55 90</span>
    </div>

    <div class="modal" style="top:92px;height:167px">
      <div class="modal-media media-portrait" role="img" aria-label="Black and white portrait of the sales manager"></div>
      <svg class="modal-arrow" style="left:11px;top:46px" viewBox="0 0 6 14"><polyline points="5,1 1,7 5,13" fill="none" stroke="#9fdff0" stroke-width=".8"/></svg>
      <svg class="modal-arrow" style="right:11px;top:46px" viewBox="0 0 6 14"><polyline points="1,1 5,7 1,13" fill="none" stroke="#9fdff0" stroke-width=".8"/></svg>
      <h5 style="top:108px">Sales Manager</h5>
      <p style="top:121px">Helps each client choose the right lights and panels for their space, prepares clear quotes and follows every order from the first call to the final install. Always happy to answer questions about costs, savings and what to expect once the new system is running.</p>
      <span class="modal-link" style="top:156px">Contact us</span>
    </div>
  </div>

</div>
</body>
</html>
```